Organic rose water based skincare line in need of product label and packaging design

We are looking for a simple, clean, modern labeling and packaging design for 2 of our products. Our brand's demographic is upscale females ages 20-40. We want our packaging to be very minimalistic, and instagramable.

Product #1: Rose water facial spray "Lilac Mist"
Product #2: Rose water facial toner "The Late Hour"

Please see attached images for our current logo and label design. We have also added some images that inspire our branding.

Target Market(s)

trendy woman ages 20-40

Industry/Entity Type

Skin Care Product

Font styles to use
Serif
Sans Serif

Colors

Designer to choose only greyscale colors for use in the design.

Requirements
Must have
• Must have our logo, bottle size, product name on front and how to use and ingredient on the back. Please see project description and attached images for more information.
Should not have
• Too much going on or too many colors.

```html
<!DOCTYPE html>
<html lang="en">
<head>
<meta charset="utf-8">
<title>Fern &amp; Bloom — Label Set</title>
<link rel="stylesheet" href="https://fonts.googleapis.com/css2?family=Arimo:wght@400&family=Roboto+Condensed:wght@300;700&display=swap">
<style>
  :root {
    --backdrop: #8a9fa0;
    --ink: #000000;
    --paper: #ffffff;
    --bloom-tone: #6b6b6b;
    --bloom-tone-light: #9a9a9a;
    --box-edge: #7a7a7a;
  }
  * { box-sizing: border-box; margin: 0; padding: 0; }
  html, body { width: 1200px; height: 808px; overflow: hidden; }
  body {
    background: var(--backdrop);
    position: relative;
    font-family: "Arimo", Arial, sans-serif;
    color: var(--paper);
  }
  .panel { position: absolute; overflow: hidden; }
  .panel--front { background: var(--ink); color: var(--paper); }
  .panel--back { background: var(--paper); color: var(--ink); text-align: center; }

  .box-front { left: 64px; top: 73px; width: 262px; height: 667px; border: 1px solid var(--box-edge); }
  .label-front { top: 220px; width: 192px; height: 380px; border-radius: 12px 0 0 12px; }
  .label-back { top: 220px; width: 192px; height: 380px; border-radius: 0 12px 12px 0; }
  .toner.label-front { left: 345px; }
  .toner.label-back { left: 538px; }
  .mist.label-front { left: 752px; }
  .mist.label-back { left: 945px; }

  .brand-name {
    position: absolute;
    font-family: "Roboto Condensed", "Arial Narrow", sans-serif;
    font-weight: 300;
    line-height: 0.82;
    color: var(--paper);
  }
  .box-front .brand-name { left: 31px; top: 110px; font-size: 23px; }
  .label-front .brand-name { left: 13px; top: 40px; font-size: 22px; }

  .bloom-art {
    position: absolute;
    background: linear-gradient(160deg, var(--bloom-tone-light) 0%, var(--bloom-tone) 40%, #1a1a1a 85%, var(--ink) 100%);
    border-radius: 40px 40px 6px 6px;
  }
  .box-front .bloom-art { left: 146px; top: 105px; width: 84px; height: 176px; }
  .label-front .bloom-art { left: 88px; top: 38px; width: 90px; height: 94px; }

  .product-name {
    position: absolute;
    font-family: "Roboto Condensed", "Arial Narrow", sans-serif;
    font-weight: 300;
    line-height: 0.98;
    text-transform: uppercase;
    color: var(--paper);
  }
  .product-name strong { font-weight: 700; }
  .box-front .product-name { left: 31px; top: 213px; font-size: 38px; }
  .label-front .product-name { left: 13px; top: 141px; font-size: 36px; }
  .mist.label-front .product-name { top: 178px; }

  .product-type {
    position: absolute;
    left: 0; right: 0;
    text-align: center;
    line-height: 1.25;
    font-weight: 400;
  }
  .box-front .product-type { top: 445px; font-size: 17px; }
  .label-front .product-type { top: 283px; font-size: 14.5px; }

  .volume {
    position: absolute;
    left: 0; right: 0;
    text-align: center;
  }
  .box-front .volume { top: 610px; font-size: 16px; }
  .label-front .volume { top: 341px; font-size: 13.5px; }

  .directions {
    position: absolute;
    left: 20px; right: 20px;
    top: 35px;
    font-size: 11.5px;
    line-height: 1.3;
  }
  .directions p + p { margin-top: 14px; }

  .ingredient {
    position: absolute;
    left: 0; right: 0;
    font-size: 17px;
    font-weight: 400;
    line-height: 1.15;
  }
  .toner .ingredient { top: 155px; }
  .mist .ingredient { top: 118px; }

  .benefits {
    position: absolute;
    left: 20px; right: 20px;
    list-style: none;
    font-size: 11.5px;
    line-height: 1.3;
  }
  .toner .benefits { top: 207px; }
  .mist .benefits { top: 191px; }
  .benefits li::before { content: "• "; }
</style>
</head>
<body>

  <section class="panel panel--front box-front">
    <div class="brand-name">fern<br>&amp;<br>bloom</div>
    <div class="bloom-art" role="img" aria-label="Line drawing of a single rose with stem and leaves"></div>
    <h1 class="product-name">The<br><strong>Late</strong><br>Hour</h1>
    <p class="product-type">Organic Rose<br>Facial Toner</p>
    <p class="volume">4 oz / 120ml</p>
  </section>

  <section class="panel panel--front label-front toner">
    <div class="brand-name">fern<br>&amp;<br>bloom</div>
    <div class="bloom-art" role="img" aria-label="Line drawing of a single rose with stem and leaves"></div>
    <h2 class="product-name">The<br><strong>Late</strong><br>Hour</h2>
    <p class="product-type">Organic Rose<br>Facial Toner</p>
    <p class="volume">4 oz / 120ml</p>
  </section>
  <section class="panel panel--back label-back toner">
    <div class="directions">
      <p>Shake well.</p>
      <p>Apply a small amount of<br>toner to a clean cotton pad<br>and gently sweep over your<br>face &amp; neck.</p>
    </div>
    <h3 class="ingredient">Witchhazel Rose</h3>
    <ul class="benefits">
      <li>Tightens skin</li>
      <li>Shrinks pores</li>
      <li>Prevents acne</li>
      <li>Treats discoloration</li>
      <li>Removes impurities</li>
    </ul>
  </section>

  <section class="panel panel--front label-front mist">
    <div class="brand-name">fern<br>&amp;<br>bloom</div>
    <div class="bloom-art" role="img" aria-label="Line drawing of a single rose with stem and leaves"></div>
    <h2 class="product-name">Lilac<br><strong>Mist</strong></h2>
    <p class="product-type">Organic Rosewater<br>Hydrating Spray</p>
    <p class="volume">4 oz / 120ml</p>
  </section>
  <section class="panel panel--back label-back mist">
    <div class="directions">
      <p>Mist over<br>face + body + hair<br>as desired for hydration.</p>
    </div>
    <h3 class="ingredient">Organic<br>Rose Water</h3>
    <ul class="benefits">
      <li>Hydrates</li>
      <li>Fights acne</li>
      <li>Maintains skin's pH</li>
      <li>Strengthens skin cells</li>
      <li>Prevents fine lines &amp;<br>wrinkles</li>
    </ul>
  </section>

</body>
</html>
```